Food packaging label design

The product name Crispelle, a thin, crispy, and delicious biscuit/cookie made from simple, all natural ingredients. Its name comes from the fact that it looks and tastes a lot like a biscotti cookie, but thinly sliced and much crispier and more delicious than a biscotti. There are currently two flavors: Pure Nutlets, and Almond Cranberry.

I am looking for a fresh, eye catchy design to go on the label for a rice paper stand up pouch (pouch sample attached). Label size are as follows:

4 oz bag - Width X Height
top: 4.5" x 3.5" bottom: 4.5" x 1.5"

12 oz bag
top: 6.5" x 5.5" bottom: 6.5" x 1.5"

I would like for the top portion of the packaging to include:

Crispelle name
Tag line " a thinner, crispier, and more delicious cousin to the biscotti"
simple and natural ingredients

bottom to include:
net weight
ingredients: wheat flour, eggs, sugar, almonds

Attached is a copy of something I created in powerpoint. you can recreate this using graphic designer software per label specs and improve on it or supprise me with something totally awesome. The key is that it that the colors and design needs to pop or contrast against the white rice paper bag and design needs to be eye catchy, fun and whimsical.

Please refer to link below for best practices for creating artwork for labels to ensure correct format for printing.
http://www.vantorprint.example/label-articles/best-practices-designing-custom-labels/

Good luck!

Target Market(s)

educated, health conscious consumers such as customers who shops at meadow pantry, brewvane, market hollis

Industry/Entity Type

Graphic Designer

Requirements
Should not have
• busy or clutter design

```html
<!DOCTYPE html>
<html lang="en">
<head>
<meta charset="utf-8">
<title>Crispelle – Pouch Labels</title>
<link rel="stylesheet" href="https://fonts.googleapis.com/css2?family=Questrial&family=Rajdhani:wght@400;500;600&family=Parisienne&display=swap">
<style>
  :root {
    --page: #ffffff;
    --label-border: #1a1a1a;
    --cream: #f2e9df;
    --cream-deep: #e7dfd3;
    --frame-ink: #24180c;
    --logo-ink: #1e1509;
    --maroon: #6a1a0c;
    --dark-ink: #1c1a18;
    --almond-light: #e3a25a;
    --almond-dark: #b9682a;
  }
  * { box-sizing: border-box; margin: 0; padding: 0; }
  html, body {
    width: 1200px; height: 900px; overflow: hidden;
    background: var(--page);
  }
  .sheet { position: relative; width: 1200px; height: 900px; }

  .label {
    position: absolute; top: 13px;
    width: 559px; height: 868px;
    border: 2px solid var(--label-border);
    background: var(--page);
    overflow: hidden;
  }
  .label--plain { left: 13px; }
  .label--cranberry { left: 610px; }

  /* top panel */
  .label__top {
    position: absolute; left: 0; top: 0;
    width: 100%; height: 437px;
    background: var(--cream);
  }
  .label__almond-strip {
    position: absolute; left: 0; top: 0;
    width: 100%; height: 31px;
    background: linear-gradient(180deg, var(--almond-dark), var(--almond-light) 55%, rgba(227,162,90,0.15));
  }
  .label__badge {
    position: absolute; left: 50%; top: 98px;
    width: 490px; height: 230px;
    transform: translateX(-50%);
  }
  .label__badge svg { position: absolute; inset: 0; }
  .label__brand {
    position: absolute; inset: 0;
    display: flex; align-items: center; justify-content: center;
    font-family: "Questrial", sans-serif;
    font-weight: 400; font-size: 74px;
    letter-spacing: -1px;
    color: var(--logo-ink);
  }

  .label__tagline-row {
    position: absolute; left: 0; top: 356px;
    width: 100%; height: 70px;
    display: flex; align-items: center; justify-content: center;
  }
  .flavor {
    text-align: center; line-height: 1;
    padding-right: 12px;
    color: var(--dark-ink);
    text-shadow: 0 0 4px #fff, 0 0 8px #fff;
  }
  .flavor__caps {
    font-family: "Rajdhani", sans-serif; font-weight: 500;
    font-size: 24px;
  }
  .flavor__caps--italic { font-style: italic; }
  .flavor__script {
    font-family: "Parisienne", cursive; font-size: 34px;
  }
  .tagline {
    border-left: 1.5px solid var(--maroon);
    padding-left: 12px;
    font-family: "Rajdhani", sans-serif; font-weight: 500;
    font-size: 23px; line-height: 28px;
    color: var(--maroon);
    text-transform: uppercase;
  }
  .tagline__light { font-weight: 400; }
  .tagline__strong { font-weight: 600; }

  /* bottom panel */
  .label__bottom {
    position: absolute; left: 0; bottom: 0;
    width: 100%; height: 185px;
    background: var(--cream);
  }
  .slogan {
    position: absolute; left: 0; top: 44px; width: 100%;
    text-align: center;
    font-family: "Parisienne", cursive; font-size: 44px;
    color: var(--dark-ink);
    text-shadow: 0 0 4px #fff, 0 0 10px #fff;
  }
  .ingredients {
    position: absolute; left: 0; top: 110px; width: 100%;
    text-align: center;
    font-family: "Rajdhani", sans-serif; font-weight: 500;
    font-size: 21px; letter-spacing: 0.3px;
    color: var(--maroon);
  }
  .ingredients__title { font-weight: 600; letter-spacing: 1px; }
  .net-weight {
    position: absolute; right: 12px; bottom: 10px;
    font-family: "Rajdhani", sans-serif; font-weight: 600;
    font-size: 14px; color: var(--dark-ink);
  }
</style>
</head>
<body>
<main class="sheet">

  <article class="label label--plain">
    <section class="label__top">
      <div class="label__almond-strip" role="img" aria-label="Row of whole almonds along the top edge"></div>
      <div class="label__badge">
        <svg viewBox="0 0 490 230" width="490" height="230" aria-hidden="true">
          <rect x="8" y="28" width="474" height="174" rx="46" fill="var(--cream-deep)" stroke="#fbf6ef" stroke-width="10"/>
          <rect x="8" y="28" width="474" height="174" rx="46" fill="none" stroke="var(--frame-ink)" stroke-width="4"/>
        </svg>
        <h1 class="label__brand">CRISPELLE</h1>
      </div>
      <div class="label__tagline-row">
        <div class="flavor">
          <div class="flavor__caps flavor__caps--italic">PURE</div>
          <div class="flavor__script">Nutlets</div>
        </div>
        <p class="tagline">
          A <span class="tagline__light">thinner</span>, <span class="tagline__strong">crispier</span>, and more<br>delicious cousin to the biscotti
        </p>
      </div>
    </section>
    <section class="label__bottom">
      <p class="slogan">Simple and Natural</p>
      <p class="ingredients"><span class="ingredients__title">INGREDIENTS</span>: Wheat flour, Eggs, Sugar, Almonds</p>
      <p class="net-weight">NET WT. 2 OZ.</p>
    </section>
  </article>

  <article class="label label--cranberry">
    <section class="label__top">
      <div class="label__almond-strip" role="img" aria-label="Row of whole almonds along the top edge"></div>
      <div class="label__badge">
        <svg viewBox="0 0 490 230" width="490" height="230" aria-hidden="true">
          <rect x="8" y="28" width="474" height="174" rx="46" fill="var(--cream-deep)" stroke="#fbf6ef" stroke-width="10"/>
          <rect x="8" y="28" width="474" height="174" rx="46" fill="none" stroke="var(--frame-ink)" stroke-width="4"/>
        </svg>
        <h1 class="label__brand">CRISPELLE</h1>
      </div>
      <div class="label__tagline-row">
        <div class="flavor">
          <div class="flavor__script">Almond</div>
          <div class="flavor__caps">CRANBERRY</div>
        </div>
        <p class="tagline">
          A <span class="tagline__light">thinner</span>, <span class="tagline__strong">crispier</span>, and more<br>delicious cousin to the biscotti
        </p>
      </div>
    </section>
    <section class="label__bottom">
      <p class="slogan">Simple and Natural</p>
      <p class="ingredients"><span class="ingredients__title">INGREDIENTS</span>: Wheat Flour, Eggs, Sugar, Almonds, Cranberry</p>
      <p class="net-weight">NET WT. 2 OZ.</p>
    </section>
  </article>

</main>
</body>
</html>
```